Brochure for Specialist Divorce Support

1. I want an A4 three fold brochure or DL to promote my business and services.
My market are people going through divorce and are usually feeling very overwhelmed and therefore not functioning very well - both men and women, age early forties,
2. Colours – variety of blues and lime greens but you choose if you need a contrast e.g. orange
3. Images – happy single families
4. Theme - could you make it around water please - soothing
5. Logos – HWN &; HWT (I will attach)
6. I have a lot of content so maybe not too busy but still professional feel +
warm and reassuring
7. I'm attaching -

- a draft brochure I put together using a Microsoft template
- a word document with extra details
- plus two logos to do with my qualifications
- and some images for you to choose from

7. I want to use this as a template for some other brochures -> more work for
the winner.

Target Market(s)

Men and women usually in their early forties with primary school aged children i.e 5 to 12 years old.
They are going through a divorce and very upset, Maybe losing contact with their children and their way of life as they know it is disappearing. They are in turmoil and not functioning as well as they usually do.

Industry/Entity Type

Business

Font styles to use
Sans Serif

Colors
34a7d7
abd037
3277b5

Requirements
Must have
• I want the brochure to be three folds with the center the full A4
• Could you make the theme around water please.
• I will upload some photos for you to use if you want,

```html
<!DOCTYPE html>
<html lang="en">
<head>
<meta charset="utf-8">
<title>Tailored Divorce Coaching Brochure</title>
<link href="https://fonts.googleapis.com/css2?family=League+Gothic&family=Oswald:wght@400;500;600&family=Roboto+Condensed:wght@400;700&display=swap" rel="stylesheet">
<style>
:root{
  --blue:#34a7d7;
  --lime:#abd037;
  --navy:#3277b5;
  --ink:#2a2a2a;
  --dark:#333333;
  --white:#ffffff;
}
*{margin:0;padding:0;box-sizing:border-box}
html,body{width:1200px;height:1200px;overflow:hidden;background:var(--white)}
body{position:relative;font-family:"Roboto Condensed",sans-serif;color:var(--ink)}
.spread{position:absolute;left:206px;width:787px;height:559px;overflow:hidden}
.spread--outside{top:28px}
.spread--inside{top:603px}
.panel{position:absolute;top:0;height:559px;overflow:hidden}
.panel--a{left:0;width:264px}
.panel--b{left:264px;width:259px}
.panel--c{left:523px;width:264px}
.display{font-family:"League Gothic",sans-serif;font-weight:400;line-height:.9;text-transform:uppercase;white-space:nowrap}
.abs{position:absolute}
.overlay{position:absolute;left:0;top:0;width:787px;height:559px;pointer-events:none}

.brand{display:flex;align-items:center;gap:4px;font-family:"Oswald",sans-serif;font-weight:600;font-size:15px;color:var(--navy)}
.brand__dot{width:10px;height:10px;border-radius:50%;background:var(--navy)}
.brand__sq{width:10px;height:10px;background:var(--navy)}

/* cover */
.cover-photo{position:absolute;left:0;top:0;width:264px;height:315px;background:linear-gradient(160deg,#c9c3bb 0%,#8d837a 45%,#3b3431 100%)}
.logo-strip{position:absolute;left:0;top:15px;width:265px;height:27px;background:var(--white);display:flex;align-items:center;gap:50px;padding-left:42px}
.cover-band{position:absolute;left:0;top:315px;width:264px;height:85px;background:var(--lime);padding:7px 0 0 16px}
.cover-band .display{font-size:43px;line-height:.88}
.cover-band .l1{color:var(--white)}
.cover-band .l2{color:var(--dark)}
.cover-copy{position:absolute;left:0;top:400px;width:264px;height:159px;background:var(--blue);padding:11px 40px 0 17px;color:var(--white);font-size:15px;line-height:13px;letter-spacing:-.6px}
.cover-copy p{margin-bottom:13px}

/* stages */
.stages{background:var(--blue);color:var(--white)}
.stages__title{position:absolute;right:12px;top:12px;text-align:right;font-size:38px;color:var(--white)}
.stage-head{position:absolute;left:32px;width:227px;height:30px;background:var(--lime);color:var(--ink);padding:2px 0 0 9px}
.stage-head b{display:block;font-family:"Oswald",sans-serif;font-weight:600;font-size:16px;line-height:16px;letter-spacing:-.6px}
.stage-head small{display:block;font-size:7.5px;line-height:9px;padding-left:14px}
.stage-text{position:absolute;left:32px;width:222px;font-size:6.5px;line-height:7.4px;text-align:justify}
.stage-text ul{list-style:none}
.stage-text li::before{content:"";display:inline-block;width:4px;height:4px;background:var(--lime);margin-right:3px}
.stages__pace{position:absolute;left:16px;top:480px;font-size:27px;color:var(--lime);line-height:.86}

/* benefits */
.benefits{background:var(--lime)}
.benefits__title1{position:absolute;left:44px;top:6px;font-size:76px;color:var(--white)}
.benefits__title2{position:absolute;left:12px;top:72px;font-size:66px;color:var(--dark)}
.bignum{position:absolute;font-family:"League Gothic",sans-serif;font-size:62px;line-height:1;color:rgba(255,255,255,.32)}
.benefit{position:absolute;width:108px;text-align:center;font-size:11.5px;line-height:13px;letter-spacing:-.4px;color:#2e2e2e}
.benefits__note{position:absolute;left:0;top:434px;width:264px;text-align:center;color:var(--white);font-size:10.8px;line-height:13px;letter-spacing:-.3px}
.benefits__contact{position:absolute;left:0;top:474px;width:264px;text-align:center;color:var(--white);font-size:13px;line-height:13.5px;letter-spacing:-.4px}
.phone{position:absolute;background:var(--blue);color:var(--white);font-family:"League Gothic",sans-serif;text-align:center;white-space:nowrap}
.benefits .phone{left:46px;top:511px;width:186px;height:38px;font-size:44px;line-height:40px}

/* inside */
.testimonial{background:linear-gradient(180deg,#0f180b 0%,#2b3d1c 45%,#15200e 100%)}
.testimonial__title{position:absolute;left:0;width:264px;top:56px;text-align:center;font-size:62px;color:var(--white)}
.testimonial__text{position:absolute;left:38px;width:192px;top:160px;text-align:center;color:var(--white);font-size:13.4px;line-height:14px;letter-spacing:-.6px}
.testimonial__name{margin-top:12px}
.testimonial .phone{left:37px;top:486px;width:183px;height:46px;font-size:50px;line-height:48px}
.scene{background:linear-gradient(180deg,#25320f 0%,#7c9a2c 35%,#a7c544 55%,#56702a 80%,#2d3b16 100%)}
.scene__caption{position:absolute;left:38px;top:366px;width:198px;color:var(--white);font-family:"Oswald",sans-serif;font-size:11.5px;line-height:17.6px;letter-spacing:-.4px;text-transform:uppercase}
.logo-bar{position:absolute;left:221px;top:486px;width:302px;height:46px;background:var(--white);display:flex;align-items:center;gap:50px;padding-left:80px}
.services{background:var(--blue);color:var(--white)}
.service{position:absolute;left:26px;width:222px;font-size:17px;line-height:19.7px;letter-spacing:-.7px}
.services__title{position:absolute;left:32px;top:480px;font-size:60px;color:var(--white)}
</style>
</head>
<body>

<section class="spread spread--outside">
  <div class="panel panel--a cover">
    <div class="cover-photo" role="img" aria-label="Photo of a smiling mother hugging her young daughter on a city street"></div>
    <div class="logo-strip">
      <span class="brand"><span class="brand__dot"></span>HWT</span>
      <span class="brand"><span class="brand__sq"></span>HWN</span>
    </div>
    <div class="cover-band">
      <div class="display l1">Tailored Divorce</div>
      <div class="display l2">Coaching/Support</div>
    </div>
    <div class="cover-copy">
      <p>Helping you successfully navigate this major life challenge . . .</p>
      <p>and move forward to your new life! Together we will identify your goals, set priorities and develop a plan for tomorrow . . .</p>
      <p>moving you through the pain of divorce.</p>
    </div>
  </div>

  <div class="panel panel--b stages">
    <div class="display stages__title">You will go through<br>distinct stages</div>

    <div class="stage-head" style="top:92px"><b>1.The Preparation Stage</b><small>maybe entail one or two coaching sessions</small></div>
    <div class="stage-text" style="top:125px"><b>Anticipating all the unknowns and preparing</b> before you see a Family Law Solicitor can save a lot of your solicitor's time and therefore money. The clearer you are on what you want to achieve throughout the process, <b>the more specific legal advice you will receive.</b></div>

    <div class="stage-head" style="top:165px"><b>2.The Business Side of Divorce</b><small>maybe two to four coaching sessions</small></div>
    <div class="stage-text" style="top:199px">
      <b>Divorce involves multiple areas of change, intensity of emotions, life changing decisions, loss of family structure and often a sense of isolation not experienced before.</b><br><br>
      The emotional overwhelm associated with relationship breakdown and the associated loss of 24/7 contact with children can impact even the most together person's ability to make well considered decisions. <b>Together, we will process emotions</b> constructively and clarify decisions to be made... for you to be better able to communicate these in negotiations as well as set new boundaries.<br><br>
      <b>Where necessary we can work on skills you will need for successful outcomes:</b>
      <ul>
        <li>conflict resolution skills plus specific verbal &amp; written communication skills important for more neutral emails and messages</li>
        <li>having difficult conversations</li>
        <li>preparing before attending joint conferences or mediation</li>
        <li>managing anger</li>
        <li>supporting your children to also navigate changed family structures</li>
        <li>grieving losses ... even if you are the one who made the decision to leave</li>
        <li>strategies for you to start healing and become whole again</li>
        <li>drafting a parenting plan to anticipate &amp; address possible parenting issues, leading to more positive and successful co-parenting in the long term. This is in everyone's interests... especially your children's.</li>
        <li>look at possible stress strategies to sustain your energy levels, important for you to make good considered decisions</li>
      </ul>
    </div>

    <div class="stage-head" style="top:400px"><b>3.The Moving On Stage</b><small>one or two coaching sessions</small></div>
    <div class="stage-text" style="top:435px">
      <b>Dealing with endings and focusing on the future:</b>
      <ul>
        <li>changing your "self" image and building self worth</li>
        <li>transitioning from married life to being single again</li>
        <li>address barriers preventing you from moving forward</li>
        <li>setting realistic goals to help transition to your new life more effectively</li>
      </ul>
    </div>

    <div class="display stages__pace">Everyone is different and<br>moves through the stages<br>at their own pace.</div>
  </div>

  <div class="panel panel--c benefits">
    <span class="bignum" style="left:8px;top:172px">01</span>
    <span class="bignum" style="left:92px;top:262px">02</span>
    <span class="bignum" style="left:8px;top:330px">03</span>
    <span class="bignum" style="left:100px;top:398px">04</span>
    <span class="bignum" style="left:132px;top:172px">05</span>
    <span class="bignum" style="left:222px;top:222px">06</span>
    <span class="bignum" style="left:132px;top:315px">07</span>
    <span class="bignum" style="left:218px;top:398px">08</span>

    <div class="display benefits__title1">Coaching</div>
    <div class="display benefits__title2">Can help you</div>

    <div class="benefit" style="left:18px;top:152px">Save money by being a more collected and credible client in the legal process</div>
    <div class="benefit" style="left:18px;top:217px">Stay in control and focus on what's important for you and your family to avoid angry, emotional hijacks</div>
    <div class="benefit" style="left:18px;top:296px">Feel more empowered by being organised and prepared for what's ahead and develop a plan of action</div>
    <div class="benefit" style="left:18px;top:374px">Identify your next steps re:legal, financial, children's issues plus your self-care</div>
    <div class="benefit" style="left:140px;top:152px">Develop a draft parenting plan to anticipate and address possible issues</div>
    <div class="benefit" style="left:140px;top:204px">Consider areas of possible conflict and explore techniques to reduce confrontation</div>
    <div class="benefit" style="left:140px;top:270px">Find your voice and be more confident in your skills to take control of your divorce and do it your way</div>
    <div class="benefit" style="left:140px;top:347px">Let go of what was ... and create what is possible during your divorce journey and afterwards.</div>

    <div class="benefits__note">Coaching works well over the phone,<br>allowing for flexibility of time and place -<br>evening appointments available.</div>
    <div class="benefits__contact">SeparationCoachingHub.com.au<br>or email:helen@partingwellhelp.com.au</div>
    <div class="phone">0400 555 123</div>
  </div>

  <svg class="overlay" viewBox="0 0 787 559" aria-hidden="true">
    <line x1="241" y1="20" x2="241" y2="38" stroke="var(--navy)" stroke-width="1.5"/>
    <polyline points="246,21 254,29 246,37" fill="none" stroke="var(--navy)" stroke-width="1.5"/>
    <polyline points="228,480 277,512 228,559" fill="none" stroke="var(--lime)" stroke-width="1.5"/>
    <line x1="236" y1="480" x2="236" y2="522" stroke="var(--lime)" stroke-width="1.5"/>
    <line x1="539" y1="30" x2="539" y2="62" stroke="var(--navy)" stroke-width="1.5"/>
    <polyline points="544,34 554,46 544,58" fill="none" stroke="var(--navy)" stroke-width="1.5"/>
  </svg>
</section>

<section class="spread spread--inside">
  <div class="panel panel--a testimonial" role="img" aria-label="Dark green photo of sunlit trees and foliage">
    <div class="display testimonial__title">Testimonial</div>
    <svg class="abs" style="left:122px;top:126px" width="22" height="14" viewBox="0 0 22 14" aria-hidden="true">
      <line x1="2" y1="2" x2="20" y2="2" stroke="#fff" stroke-width="1.4"/>
      <polyline points="3,6 11,12 19,6" fill="none" stroke="#fff" stroke-width="1.4"/>
    </svg>
    <div class="testimonial__text">
      After many cups of coffee and long hours of listening to me, my very good friend suggested I speak to Helen, a divorce coach. I was a bit skeptical, especially when a phone session was suggested.<br>
      From my first phone session I felt empowered. It gave me a sense of direction, assisted me to set realistic goals and action plans. Most importantly it aided my self esteem. Divorce is overwhelming. Talking to a caring professional like Helena helped me acknowledge my priorities and a way to achieve them. Thank you Helena.
      <div class="testimonial__name">Marisa - Ccccccc, Smmmmm. AAA</div>
    </div>
    <div class="phone">0400 555 123</div>
  </div>

  <div class="panel panel--b scene" role="img" aria-label="Photo of a father walking with his young child by a lake at sunset, tinted green">
    <div class="scene__caption">Often family and friends can try to influence decisions based on what they see as best, so you can feel under an enormous pressure to keep them happy. Coaching offers an objective and neutral sounding board there just for you.</div>
  </div>

  <div class="panel panel--c services">
    <div class="service" style="top:32px">Tailored divorce support to suit your needs</div>
    <div class="service" style="top:90px">Pre-mediation coaching helping you prepare and achieve more positive outcomes to avoid court</div>
    <div class="service" style="top:168px">Collaborative law coaching to increase crucial skills so you can participate more constructively in negotiations</div>
    <div class="service" style="top:266px">Delivery of HWN Conflict Insight Profile giving you real feedback on the constructive and destructive behaviours you choose during conflict situations to facilitate more productive discussions</div>
    <div class="service" style="top:421px">Corporate Conflict Management Training</div>
    <div class="display services__title">My Services</div>
  </div>

  <div class="logo-bar">
    <span class="brand"><span class="brand__dot"></span>HWT</span>
    <span class="brand"><span class="brand__sq"></span>HWN</span>
  </div>

  <svg class="overlay" viewBox="0 0 787 559" aria-hidden="true">
    <polyline points="493,26 547,75 471,186" fill="none" stroke="#fff" stroke-width="1.5"/>
    <line x1="507" y1="62" x2="507" y2="112" stroke="#fff" stroke-width="1.5"/>
    <polyline points="264,372 232,423 264,480" fill="none" stroke="#fff" stroke-width="1.5"/>
    <line x1="533" y1="500" x2="533" y2="522" stroke="#fff" stroke-width="1.5"/>
    <polyline points="537,504 543,511 537,518" fill="none" stroke="#fff" stroke-width="1.5"/>
  </svg>
</section>

</body>
</html>
```